Business Card Design

Looking for business card designs for a new business. there will be two cards of the same design (both lots of information below in contact info). We would like the logo diagonally across the card with the information split above and below the logo similar to sketch. happy to look at similar alternatives
Please use same colours as in logo design

Industry/Entity Type

Business

Contact Information for Business Card

Gareth Mullins
mob - 0498 172 309
ph - 02 4839 2100
fax - 02 4839 2400
email - gaz@ridgelinetrusses.com.au
14 Calloway Road, Parrinda NSW 2871

Desmond Alcott
mob - 0426 918 753
ph - 02 4839 2100
fax - 02 4839 2400
email - desmond@ridgelinetrusses.com.au

```html
<!DOCTYPE html>
<html lang="en">
<head>
<meta charset="utf-8">
<title>Ridgeline Frames &amp; Trusses – Business Cards</title>
<link rel="stylesheet" href="https://fonts.googleapis.com/css2?family=Open+Sans:wght@400;700&display=swap">
<style>
  :root {
    --teal: #0f8b7f;
    --white: #ffffff;
    --ink: #111111;
    --backdrop: #e9e7e3;
    --label: #6f6a64;
  }
  html, body {
    margin: 0;
    padding: 0;
    overflow: hidden;
  }
  body {
    width: 1200px;
    height: 479px;
    background: var(--backdrop);
    font-family: "Open Sans", sans-serif;
  }
  .sheet {
    position: relative;
    width: 1200px;
    height: 479px;
    display: flex;
  }
  .card-slot {
    position: relative;
    width: 600px;
    height: 479px;
    display: flex;
    justify-content: center;
    align-items: flex-start;
    padding-top: 22px;
    box-sizing: border-box;
  }
  .card {
    width: 252px;
    height: 420px;
    filter: drop-shadow(0 3px 6px rgba(0,0,0,0.25));
  }
  .card-label {
    position: absolute;
    left: 32px;
    bottom: 14px;
    font-size: 30px;
    color: var(--label);
  }
  .card-face { fill: var(--teal); }
  .band { fill: var(--white); }
  .band-rule { fill: var(--white); }
  .holder-name { fill: var(--white); font-weight: 700; font-size: 15px; }
  .holder-detail { fill: var(--white); font-size: 9.5px; }
  .office-detail { fill: var(--white); font-size: 9.5px; }
  .office-key { font-weight: 700; }
  .brand-name { fill: var(--ink); font-weight: 700; font-size: 28px; }
  .brand-tagline { fill: var(--ink); font-weight: 700; font-size: 12px; }
  .brand-mark { fill: var(--teal); }
</style>
</head>
<body>
<main class="sheet">

  <section class="card-slot">
    <svg class="card" viewBox="0 0 252 420" aria-label="Business card for Gareth Mullins">
      <defs>
        <clipPath id="card-shape-1"><rect width="252" height="420" rx="20"/></clipPath>
      </defs>
      <g clip-path="url(#card-shape-1)">
        <rect class="card-face" width="252" height="420"/>
        <g transform="translate(126 210) rotate(-55)">
          <rect class="band-rule" x="-400" y="-44" width="800" height="4"/>
          <rect class="band" x="-400" y="-33" width="800" height="66"/>
          <rect class="band-rule" x="-400" y="40" width="800" height="4"/>

          <text class="holder-name" x="-20" y="-96">GARETH MULLINS</text>
          <text class="holder-detail" x="-4" y="-80">0498 172 309</text>
          <text class="holder-detail" x="-16" y="-66">gaz@ridgelinetrusses.com.au</text>

          <rect class="brand-mark" x="-108" y="-14" width="16" height="16"/>
          <text class="brand-name" x="-86" y="3">Ridgeline</text>
          <text class="brand-tagline" x="-86" y="20">Frames &amp; Trusses</text>

          <text class="office-detail" x="-140" y="70"><tspan class="office-key">P:</tspan> 02 4839 2100</text>
          <text class="office-detail" x="-140" y="84"><tspan class="office-key">F:</tspan> 02 4839 2400</text>
          <text class="office-detail" x="-140" y="98">14 Calloway Road, Parrinda NSW 2871</text>
        </g>
      </g>
    </svg>
    <span class="card-label">Card 1</span>
  </section>

  <section class="card-slot">
    <svg class="card" viewBox="0 0 252 420" aria-label="Business card for Desmond Alcott">
      <defs>
        <clipPath id="card-shape-2"><rect width="252" height="420" rx="20"/></clipPath>
      </defs>
      <g clip-path="url(#card-shape-2)">
        <rect class="card-face" width="252" height="420"/>
        <g transform="translate(126 210) rotate(-55)">
          <rect class="band-rule" x="-400" y="-44" width="800" height="4"/>
          <rect class="band" x="-400" y="-33" width="800" height="66"/>
          <rect class="band-rule" x="-400" y="40" width="800" height="4"/>

          <text class="holder-name" x="-20" y="-96">Desmond Alcott</text>
          <text class="holder-detail" x="-4" y="-80">0426 918 753</text>
          <text class="holder-detail" x="-20" y="-66">desmond@ridgelinetrusses.com.au</text>

          <rect class="brand-mark" x="-108" y="-14" width="16" height="16"/>
          <text class="brand-name" x="-86" y="3">Ridgeline</text>
          <text class="brand-tagline" x="-86" y="20">Frames &amp; Trusses</text>

          <text class="office-detail" x="-140" y="70"><tspan class="office-key">P:</tspan> 02 4839 2100</text>
          <text class="office-detail" x="-140" y="84"><tspan class="office-key">F:</tspan> 02 4839 2400</text>
          <text class="office-detail" x="-140" y="98">14 Calloway Road, Parrinda NSW 2871</text>
        </g>
      </g>
    </svg>
    <span class="card-label">Card 2</span>
  </section>

</main>
</body>
</html>
```